E learning Platform for privacy

Current website is as below and its more of a shell.
I need someone to take the text and content and design it properly.
https://study.norvalhub.example/

After that, design has to be implemented with quillbrick and wordpress
https://quillbrick.example/

```html
<!DOCTYPE html>
<html lang="en">
<head>
<meta charset="utf-8">
<title>Norvalhub Learning Centre – Sign In</title>
<link rel="stylesheet" href="https://fonts.googleapis.com/css2?family=Poppins:wght@400;500;600;700&display=swap">
<style>
  :root {
    --ink: #262626;
    --ink-soft: #555555;
    --muted: #7a7a7a;
    --field: #eeeff2;
    --accent: #f0931f;
    --accent-deep: #e6662f;
    --panel: #2b2b2b;
    --white: #ffffff;
    --social-a: #3c4f8f;
    --social-b: #2ea3e6;
    --social-c: #e2483a;
  }
  * { box-sizing: border-box; margin: 0; padding: 0; }
  html, body { width: 1200px; height: 836px; overflow: hidden; background: var(--white); }
  body { font-family: "Poppins", sans-serif; color: var(--ink); position: relative; }

  .hero-art { position: absolute; inset: 0; width: 1200px; height: 836px; }

  .brand {
    position: absolute; left: 88px; top: 30px;
    font-family: "Poppins", sans-serif; font-weight: 600;
    font-size: 30px; letter-spacing: 1px; color: var(--accent-deep);
  }

  .signin { position: absolute; left: 88px; top: 203px; width: 420px; }
  .signin__intro { font-size: 14px; font-weight: 600; color: var(--ink); }
  .signin__intro a { color: var(--accent); text-decoration: none; border-bottom: 1px solid var(--accent); }
  .signin__title { font-size: 60px; font-weight: 700; line-height: 1; margin-top: 16px; letter-spacing: 0.5px; }

  .field-label { display: block; font-size: 15px; font-weight: 600; letter-spacing: 0.3px; margin-top: 32px; }
  .field-label--pw { margin-top: 33px; }
  .field {
    display: block; width: 383px; height: 50px; margin-top: 5px;
    border: none; border-radius: 25px; background: var(--field);
    padding: 0 29px; font-family: "Poppins", sans-serif; font-size: 16px; color: var(--ink-soft);
  }
  .field::placeholder { color: var(--ink-soft); }
  .field-hint { font-size: 12.5px; color: var(--muted); margin-top: 8px; margin-left: -1px; }

  .forgot {
    display: inline-block; margin-top: 14px; margin-left: 2px;
    font-size: 16px; color: var(--ink); text-decoration: none;
    border-bottom: 1px solid var(--ink); line-height: 1.2;
  }
  .login-btn {
    display: block; width: 383px; height: 50px; margin-top: 40px;
    border: none; border-radius: 25px; background: var(--accent);
    color: var(--white); font-family: "Poppins", sans-serif; font-size: 20px; font-weight: 600;
  }
  .social { display: flex; gap: 7px; justify-content: center; width: 383px; margin-top: 30px; }
  .social__item { width: 40px; height: 40px; border-radius: 50%; display: block; }
  .social__item--a { background: var(--social-a); }
  .social__item--b { background: var(--social-b); }
  .social__item--c { background: var(--social-c); }
</style>
</head>
<body>
  <svg class="hero-art" viewBox="0 0 1200 836" role="img" aria-label="Illustration: a student with a laptop sitting by a wall clock on a dark patterned backdrop">
    <path fill="var(--accent-deep)" d="M600 520 C650 580 740 603 810 598 C880 593 920 548 1000 548 C1080 548 1120 600 1200 584 L1200 570 C1120 585 1080 535 1000 535 C920 535 880 580 810 585 C740 590 660 575 600 520 Z"/>
    <path fill="var(--panel)" d="M450 0 C440 90 470 150 530 185 C590 220 590 280 580 340 C565 420 560 480 610 530 C660 580 740 595 810 590 C880 585 920 540 1000 540 C1080 540 1120 590 1200 575 L1200 0 Z"/>
  </svg>

  <div class="brand">Norvalhub</div>

  <main class="signin">
    <p class="signin__intro">First time here? <a href="#">Create an account</a></p>
    <h1 class="signin__title">Sign In</h1>

    <form>
      <label class="field-label" for="email">EMAIL</label>
      <input class="field" id="email" type="email" placeholder="Username@domain.com">
      <p class="field-hint">The email address you used to register with Norvalhub Learning Centre</p>

      <label class="field-label field-label--pw" for="password">PASSWORD</label>
      <input class="field" id="password" type="password" value="**********">

      <a class="forgot" href="#">Forgot Password?</a>

      <button class="login-btn" type="button">LOGIN</button>
    </form>

    <nav class="social" aria-label="Sign in with a social account">
      <a class="social__item social__item--a" href="#" aria-label="Social sign-in option one"></a>
      <a class="social__item social__item--b" href="#" aria-label="Social sign-in option two"></a>
      <a class="social__item social__item--c" href="#" aria-label="Social sign-in option three"></a>
    </nav>
  </main>
</body>
</html>
```